Attorney Recruiting company needs brochure

Brief Harbor is a company that recruits attorneys for law firms and corporations. We want a brochure that makes the law firms and corporation want to retain us to recruit attorneys when they are hiring. We identify experienced well qualified attorneys. We provide them for direct hire (also knows as permanent placement) and for temporary contract hourly work. We want our colors included: red, black and white. It has to convey professionalism and experience. You can find lots of information about who we are and what we do on our website. www.briefharbor-example.com. The brochure should be in traditional conservative font. Should be easy to read. Attorneys tend to scan brochures to see what we do, they will need read it word for word, so we don't need lots of paragraphs and extraneous text. The brochure should outline easily the services we provide which are very specific. They are outlined on home page of website. You should also include our logo which I will attach in several formats.

Target Market(s)

Attorneys and executives

Industry/Entity Type

Conservative

Requirements
Must have
• logo
colors described above

```html
<!DOCTYPE html>
<html lang="en">
<head>
<meta charset="utf-8">
<title>Brief Harbor – How We Recruit Attorneys</title>
<link rel="stylesheet" href="https://fonts.googleapis.com/css2?family=Tinos:ital,wght@0,400;0,700;1,700&display=swap">
<style>
  :root {
    --black: #000000;
    --panel-black: #0b0b0b;
    --red: #a50000;
    --white: #ffffff;
    --ink: #161616;
    --muted: #b9b9b9;
    --caption: #2a2a2a;
  }
  * { margin: 0; padding: 0; box-sizing: border-box; }
  html, body { width: 1200px; height: 930px; overflow: hidden; background: var(--white); }
  body { font-family: "Tinos", "Times New Roman", serif; }

  .brochure-panel { position: relative; width: 1200px; height: 930px; overflow: hidden; background: var(--white); }

  .top-band { position: absolute; left: 0; top: 0; width: 1200px; height: 145px; background: var(--black); }

  .testimonial-column { position: absolute; left: 0; top: 0; width: 395px; height: 930px; background: var(--panel-black); }

  .column-title {
    position: absolute; left: 35px; top: 44px;
    color: var(--white); font-weight: 700; font-size: 37px; line-height: 37px; letter-spacing: 1px;
  }
  .section-title {
    position: absolute; left: 422px; top: 80px;
    color: var(--white); font-weight: 700; font-size: 33px; letter-spacing: 0.6px;
  }

  .quote { position: absolute; color: var(--white); }
  .quote-mark {
    position: absolute; font-style: italic; font-weight: 700;
    font-size: 82px; line-height: 1; color: var(--white);
  }
  .quote-body {
    font-weight: 700; font-size: 16px; line-height: 21.1px; letter-spacing: 2.2px;
  }
  .quote-source { font-size: 11px; letter-spacing: 0.8px; color: var(--muted); line-height: 14px; }

  .quote--discovery { left: 55px; top: 161px; width: 330px; }
  .quote--discovery .quote-mark { left: -28px; top: -40px; }
  .quote--discovery .quote-source { margin: 8px 0 0 42px; }

  .quote--specialist { left: 55px; top: 643px; width: 320px; }
  .quote--specialist .quote-mark { left: -28px; top: -37px; }
  .quote--specialist .quote-source { margin: 10px 0 0 92px; }

  .process-panel {
    position: absolute; left: 395px; top: 145px; width: 805px; height: 477px;
    background: var(--red); color: var(--white);
  }
  .process-step { position: absolute; left: 42px; width: 740px; }
  .step-heading { font-weight: 700; font-size: 16px; letter-spacing: 0.4px; margin-bottom: 6px; }
  .step-body { font-size: 13.6px; line-height: 21.6px; padding-left: 21px; letter-spacing: 0.1px; }
  .step-1 { top: 8px; }
  .step-2 { top: 144px; }
  .step-3 { top: 270px; left: 45px; }
  .step-4 { top: 380px; left: 45px; }

  .photo-area {
    position: absolute; left: 395px; top: 622px; width: 805px; height: 308px;
    background: linear-gradient(90deg, #f4f4f2 0%, #e9e9e6 40%, #cfcbc6 62%, #c9b8a8 78%, #efe9e3 100%);
  }

  .quote--thanks { left: 477px; top: 668px; width: 330px; color: var(--ink); }
  .quote--thanks .quote-mark { left: -28px; top: -36px; color: var(--ink); }
  .quote--thanks .quote-body { color: var(--ink); }
  .quote--thanks .closing { display: block; padding-left: 100px; }
  .quote--thanks .quote-source { color: var(--caption); margin: 14px 0 0 117px; }
</style>
</head>
<body>
<main class="brochure-panel">
  <div class="top-band"></div>

  <aside class="testimonial-column">
    <h2 class="column-title">What our Clients<br>are Saying:</h2>

    <figure class="quote quote--discovery">
      <span class="quote-mark" aria-hidden="true">“</span>
      <blockquote class="quote-body">Our law firm was handling a very complex litigation matter that involved hundreds of boxes of discovery. We were not staffed to get the documents reviewed in a timely manner but did not want to hire additional attorneys. We contacted Brief Harbor and they were able to provide our firm with a team of qualified contract attorneys to handle document review. This permitted our attorneys to handle more substantive matters while still being updated on discovery issues. It was a great solution to an otherwise overwhelming discovery process and we will definitely call Brief Harbor again.”</blockquote>
      <figcaption class="quote-source">- Partner, large AV rated Orlando law firm</figcaption>
    </figure>

    <figure class="quote quote--specialist">
      <span class="quote-mark" aria-hidden="true">“</span>
      <blockquote class="quote-body">We needed an attorney with very specialized legal experience. Brief Harbor understood exactly what we needed and found the perfect addition for our firm. We were able to focus on practicing law while Brief Harbor handled the recruiting process. We will definitely call Brief Harbor next time.”</blockquote>
      <figcaption class="quote-source">- Managing Shareholder,<br>&nbsp;mid size Orlando specialty firm</figcaption>
    </figure>
  </aside>

  <h1 class="section-title">How we Recruit Attorneys for Employers?</h1>

  <section class="process-panel">
    <div class="process-step step-1">
      <h3 class="step-heading">1. Meet the Employer</h3>
      <p class="step-body">We want to meet with you personally whenever possible to ensure we&nbsp; understand exactly what you need. We want to appreciate both the tangible and intangible aspects of the position. Visiting the office and meeting the people with whom the attorney will work is generally very helpful but not required.</p>
    </div>
    <div class="process-step step-2">
      <h3 class="step-heading">2. Recruit Attorneys</h3>
      <p class="step-body">We are very well networked in the legal community and have reliable referral sources in every area of law and business. We also have an established database of attorneys who are either active or passive job seekers that have confidentially requested us to let them know when the "right position" is available. When needed we also conduct general and targeted advertising.</p>
    </div>
    <div class="process-step step-3">
      <h3 class="step-heading">3. Screen Attorneys</h3>
      <p class="step-body">We interview potential candidates with our proven interview system. We conduct reference<br>checks, except where employer prefers to complete reference checks. We confirm that state<br>bar membership is in good standing where applicable.</p>
    </div>
    <div class="process-step step-4">
      <h3 class="step-heading">4. Facilitate Interview and Hiring</h3>
      <p class="step-body">We will present you with resumes and significant commentary from our screening process for the top candidates. You may only need to meet two or three attorney candidates unless you prefer to consider more. We are available to be involved in any aspect of salary and benefit negotiations.</p>
    </div>
  </section>

  <div class="photo-area" role="img" aria-label="Photo of a smiling professional woman in a white blouse in a bright office, with colleagues blurred in the background"></div>

  <figure class="quote quote--thanks">
    <span class="quote-mark" aria-hidden="true">“</span>
    <blockquote class="quote-body">Thank you for securing an exceptionally qualified attorney for our firm. You clearly understood our goals and objectives and you delivered. We won’t hesitate to contact you next time.<span class="closing">Thanks so much!”</span></blockquote>
    <figcaption class="quote-source">- Managing Shareholder,<br>AV rated national law firm</figcaption>
  </figure>
</main>
</body>
</html>
```